Optometry practice sign/banner

Modern design appeal to mix demographic, family friendly. Emphasize the importance of eye exam.
Brigh colors, green,blue, yellow,
Photo of people wearing glasses
4'x8'

" EYE EXAM, CONTACT LENS, ORTHOK, LASIK CONSULTATION, DIABETES RETINAL EXAM
DR. NINA BOLT
BRIVAX OPTOMETRY " Eyecare for your family"
626.555.0183
MEDICAL, HELIXPLAN, QTR, ZORBEN, WALK IN WELCOME"

Target Market(s)

Family, middle age, mix demographic

Colors
33b8a4
fbee3d
cee9f5
9bcb3c

Requirements
Nice to have
• Photo of family wearing glasses.

```html
<!DOCTYPE html>
<html lang="en">
<head>
<meta charset="utf-8">
<title>Brivax Optometry Banner</title>
<link rel="stylesheet" href="https://fonts.googleapis.com/css2?family=Arimo:wght@400&family=Exo+2:ital,wght@1,800&family=Montserrat:wght@600&family=Roboto+Condensed:wght@700&family=Titillium+Web:wght@600&display=swap">
<style>
  :root {
    --teal: #33b8a4;
    --teal-deep: #23907f;
    --teal-dark: #1f8a7a;
    --yellow: #fbee3d;
    --sky: #cee9f5;
    --lime: #9bcb3c;
    --gold: #f2c230;
    --white: #ffffff;
    --ink: #4a4a4a;
    --photo-light: #f2f3f1;
    --photo-warm: #dcc8b4;
    --photo-hair: #b89670;
    --backdrop: #4b4747;
  }
  * { margin: 0; padding: 0; box-sizing: border-box; }
  html, body { width: 1200px; height: 678px; overflow: hidden; background: var(--backdrop); }
  .canvas { position: relative; width: 1200px; height: 678px; overflow: hidden; }
  .banner { position: absolute; left: 70px; top: 73px; width: 1060px; height: 530px; overflow: hidden; background: var(--teal); }

  .family-photo {
    position: absolute; left: 330px; top: 0; width: 730px; height: 530px;
    background:
      radial-gradient(ellipse 34% 42% at 40% 52%, var(--photo-warm) 0%, rgba(220,200,180,0) 100%),
      radial-gradient(ellipse 30% 40% at 70% 50%, var(--photo-warm) 0%, rgba(220,200,180,0) 100%),
      radial-gradient(ellipse 22% 30% at 90% 30%, var(--photo-hair) 0%, rgba(184,150,112,0) 100%),
      radial-gradient(ellipse 20% 26% at 28% 34%, var(--photo-hair) 0%, rgba(184,150,112,0) 100%),
      linear-gradient(110deg, var(--photo-light) 0%, #e8ecea 50%, var(--sky) 100%);
  }
  .curve-shapes { position: absolute; left: 0; top: 0; width: 1060px; height: 530px; }

  .headline {
    position: absolute; left: 398px; top: 24px;
    font-family: "Exo 2", sans-serif; font-style: italic; font-weight: 800;
    font-size: 35px; letter-spacing: .5px; color: var(--teal-dark);
  }

  .brand { position: absolute; left: 32px; top: 0; width: 300px; text-align: center; color: var(--white); font-family: "Arimo", sans-serif; }
  .brand-mark { display: block; width: 106px; height: 106px; margin: 36px auto 52px; background: var(--gold); }
  .brand-name { font-size: 44px; line-height: 1; letter-spacing: 2px; }
  .brand-sub { font-size: 30px; line-height: 1; margin-top: 12px; letter-spacing: 1.5px; }

  .contact {
    position: absolute; left: 37px; top: 310px; width: 338px; height: 84px;
    border-top: 2px solid rgba(255,255,255,.85); border-bottom: 2px solid rgba(255,255,255,.85);
    background: linear-gradient(180deg, var(--teal-deep), var(--teal));
    text-align: center; padding-top: 10px;
  }
  .phone { font-family: "Montserrat", sans-serif; font-weight: 600; font-size: 29px; color: var(--white); line-height: 1.2; }
  .website { font-family: "Montserrat", sans-serif; font-weight: 600; font-size: 17px; color: var(--yellow); }

  .services {
    position: absolute; left: 24px; top: 414px; display: grid; grid-template-columns: 192px 290px;
    list-style: none; font-family: "Exo 2", sans-serif; font-style: italic; font-weight: 800;
    font-size: 19.5px; line-height: 29px; color: var(--white);
  }
  .services li::before { content: ""; display: inline-block; width: 7px; height: 7px; border-radius: 50%; background: var(--yellow); margin-right: 9px; vertical-align: middle; }
  .services li.col2 { grid-column: 2; }

  .walk-in {
    position: absolute; left: 895px; top: 317px; width: 154px; height: 154px; border-radius: 50%;
    background: var(--lime); border: 6px solid var(--white);
    display: flex; align-items: center; justify-content: center; text-align: center;
    font-family: "Roboto Condensed", sans-serif; font-weight: 700; font-size: 30px; line-height: 1.1; color: var(--yellow);
  }

  .plans { position: absolute; left: 645px; top: 479px; display: flex; gap: 10px; list-style: none;
    font-family: "Titillium Web", sans-serif; font-weight: 600; font-size: 20px; color: var(--ink); letter-spacing: .5px; }
  .plans li::before { content: ""; display: inline-block; width: 9px; height: 9px; background: var(--teal); margin-right: 6px; vertical-align: 2px; }
</style>
</head>
<body>
<div class="canvas">
  <div class="banner">
    <div class="family-photo" role="img" aria-label="Photo of a smiling family of four, parents and two children, all wearing glasses"></div>
    <svg class="curve-shapes" viewBox="0 0 1060 530" aria-hidden="true">
      <path d="M355 0 C350 230 520 440 700 530 H640 C450 450 300 250 305 0 Z" fill="var(--lime)"/>
      <path d="M0 0 H305 C300 250 450 450 640 530 H0 Z" fill="var(--teal)"/>
      <path d="M305 0 C300 250 450 450 640 530" fill="none" stroke="var(--yellow)" stroke-width="7"/>
    </svg>

    <h1 class="headline">EYECARE FOR YOUR FAMILY</h1>

    <div class="brand">
      <span class="brand-mark"></span>
      <div class="brand-name">BRIVAX</div>
      <div class="brand-sub">OPTOMETRY</div>
    </div>

    <div class="contact">
      <div class="phone">Call: 626.555.0183</div>
      <div class="website">www.brivaxsee.com</div>
    </div>

    <ul class="services">
      <li>EYE EXAM</li>
      <li class="col2">LASIK CONSULTATION</li>
      <li>CONTACT LENS</li>
      <li class="col2">DIABETES RETINAL EXAM</li>
      <li>ORTHOK</li>
    </ul>

    <div class="walk-in">WALK IN<br>WELCOME</div>

    <ul class="plans">
      <li>MEDICAL</li>
      <li>HELIXPLAN</li>
      <li>QTR</li>
      <li>ZORBEN</li>
    </ul>
  </div>
</div>
</body>
</html>
```